"Amberlane Vantage Harbor": unique end to end Chinese marketing and ecommerce solutions*

I would like to create a company website for my trademark: "Amberlane Vantage Harbor". We are based in Iceland. We are the only company in the market offering end-to-end Chinese digital marketing and eCommerce solutions. We help companies grow their brands and sales towards Chinese - whether tourism, export of products or services.
I include the logo that we have come up with in terms of colours and fonts.
The font is Trajan - I would like to use normal letters (capital and lowercase) for text.
Front page: Picture with colour filter. Logo in white. Text line underneath.
I am inspired by this website:
https://www.brindlecove.example/
I like these short videos for landing page:
https://www.pixelorchard.example/video/clip-48213907-misty-ridge-scenery
https://www.pixelorchard.example/video/clip-7390451128-4k-aerial-video-ridge-scenery
https://www.pixelorchard.example/video/clip-6620984315-ridge-scenery
Icelandic businesses looking for business opportunities in China or to attract Chinese tourists.
Digital Marketing

```html
<!DOCTYPE html>
<html lang="en">
<head>
<meta charset="utf-8">
<title>Amberlane Vantage Harbor</title>
<link rel="stylesheet" href="https://fonts.googleapis.com/css2?family=Cinzel:wght@400;600&family=Barlow:ital,wght@0,400;0,500;1,400&display=swap">
<style>
:root{
  --gold:#b0873c;
  --gold-bar:#b38e4c;
  --blue:#1a55a6;
  --blue-active:#12489c;
  --ink:#222;
  --muted:#888;
  --line:#e3e3e3;
  --white:#fff;
}
*{box-sizing:border-box;margin:0;padding:0}
html,body{width:1200px;height:3799px;overflow:hidden}
body{position:relative;background:var(--white);font-family:'Barlow',sans-serif;color:var(--ink)}
.abs{position:absolute}

/* header */
.topbar-email{left:111px;top:40px;font-size:13px;color:#333;display:flex;align-items:center;gap:6px}
.topbar-call{right:114px;top:36px;font-size:13px;color:#333;display:flex;align-items:center;gap:6px}
.topbar-call b{font-size:18px;font-weight:500}
.brand{left:482px;top:28px;display:flex;align-items:center;gap:10px}
.brand-mark{width:34px;height:34px;border-radius:50%;background:var(--gold)}
.brand-name{font-family:'Cinzel',serif;font-size:19px;color:var(--gold);line-height:1}
.nav{left:111px;top:91px;width:977px;height:62px;background:var(--gold-bar);display:flex;align-items:center;padding-left:18px;z-index:2}
.nav a{font-family:'Cinzel',serif;color:var(--white);font-size:15px;text-decoration:none;padding:6px 16px}
.nav a.active{background:var(--blue-active)}

/* hero */
.hero{left:0;top:113px;width:1200px;height:577px;
  background:
    radial-gradient(ellipse 320px 220px at 1080px 120px,rgba(245,240,230,.9),rgba(245,240,230,0) 70%),
    radial-gradient(ellipse 260px 200px at 180px 80px,rgba(240,236,228,.85),rgba(240,236,228,0) 70%),
    radial-gradient(ellipse 260px 260px at 720px 260px,rgba(70,80,95,.75),rgba(70,80,95,0) 70%),
    radial-gradient(ellipse 240px 240px at 920px 340px,rgba(40,40,45,.7),rgba(40,40,45,0) 70%),
    radial-gradient(ellipse 200px 180px at 420px 150px,rgba(200,160,130,.8),rgba(200,160,130,0) 70%),
    linear-gradient(180deg,#b9a994 0%,#a8937b 55%,#7c5d44 78%,#4e3a2c 100%)}
.hero-panel{left:0;top:258px;width:603px;height:314px;background:rgba(118,158,200,.6)}
.hero-title{left:113px;top:268px;font-family:'Cinzel',serif;font-size:56px;line-height:68px;color:var(--white);font-weight:600;text-transform:uppercase;letter-spacing:.5px}
.hero-text{left:111px;top:412px;width:460px;font-size:14.5px;line-height:33px;color:var(--white)}
.hero-btn{left:112px;top:498px;width:156px;height:53px;border:1px solid var(--white);color:var(--white);font-size:16px;display:flex;align-items:center;justify-content:center}
.hero-dots{left:112px;top:661px;display:flex;gap:12px}
.hero-dots span{width:13px;height:13px;border-radius:50%;border:1.5px solid var(--white)}
.hero-dots span.on{background:var(--white)}

/* section titles */
.section-title{width:1200px;left:0;text-align:center;font-family:'Cinzel',serif;font-weight:600;font-size:46px;color:#111;letter-spacing:1px}

/* services */
.card{top:833px;width:318px;height:473px;border:1px solid var(--line);border-radius:8px;box-shadow:0 0 6px rgba(0,0,0,.12);background:var(--white);padding:6px}
.card-photo{height:248px;border-radius:2px}
.card h3{font-family:'Cinzel',serif;font-weight:400;font-size:17px;margin:24px 0 0 4px;color:#222}
.card p{font-size:13px;line-height:26px;color:var(--muted);margin:14px 4px 0;text-align:justify}
.btn-outline{display:inline-flex;align-items:center;justify-content:center;border:1px solid var(--gold);color:var(--gold);font-size:15px;background:var(--white)}
.card .btn-outline{margin:16px 0 0 2px;width:140px;height:48px}
.round-arrow{width:44px;height:44px;border-radius:50%;border:1.5px solid #333;display:flex;align-items:center;justify-content:center;background:var(--white)}

/* video */
.video{left:0;top:1412px;width:1200px;height:481px;
  background:
    radial-gradient(ellipse 500px 140px at 600px 40px,rgba(180,180,170,.75),rgba(180,180,170,0) 75%),
    radial-gradient(ellipse 300px 260px at 360px 330px,rgba(120,105,70,.7),rgba(120,105,70,0) 70%),
    radial-gradient(ellipse 380px 220px at 900px 300px,rgba(70,85,35,.8),rgba(70,85,35,0) 70%),
    radial-gradient(ellipse 260px 200px at 120px 200px,rgba(95,105,55,.7),rgba(95,105,55,0) 70%),
    linear-gradient(180deg,#8d927f 0%,#6a7247 30%,#566231 60%,#5e5430 100%)}
.video-title{top:1464px;color:var(--white)}
.play{left:546px;top:1599px;width:104px;height:104px;border-radius:50%;background:var(--blue);display:flex;align-items:center;justify-content:center}
.video-nav{left:1088px;top:1850px;width:112px;height:43px;background:var(--white);display:flex;align-items:center;justify-content:center;gap:8px}

/* about */
.about-title{left:111px;top:2022px;font-family:'Cinzel',serif;font-weight:600;font-size:46px;color:#111}
.about-text{left:113px;top:2096px;width:465px;font-size:14.5px;line-height:34.2px;color:var(--muted);text-align:justify}
.about-btn{left:112px;top:2322px;width:156px;height:52px;font-size:17px}
.about-photo{left:618px;top:1994px;width:464px;height:419px;box-shadow:0 0 4px rgba(0,0,0,.2);
  background:
    radial-gradient(ellipse 140px 120px at 200px 140px,rgba(60,45,40,.75),rgba(60,45,40,0) 70%),
    radial-gradient(ellipse 120px 130px at 130px 260px,rgba(40,80,100,.6),rgba(40,80,100,0) 70%),
    radial-gradient(ellipse 170px 90px at 300px 320px,rgba(235,235,232,.9),rgba(235,235,232,0) 70%),
    linear-gradient(180deg,#7f8d96 0%,#a9b0b4 40%,#cfd1cf 70%,#9a9995 100%)}

/* blogs */
.blogs-sub{left:0;width:1200px;top:2566px;text-align:center;font-size:14.5px;line-height:26px;color:#555}
.blog{top:2646px;width:317px;height:255px;color:var(--white);font-size:13px;line-height:24px}
.blog-body{position:absolute;left:17px}
.blog .more{text-decoration:underline;font-weight:500;display:flex;align-items:center;gap:6px;margin-top:12px}
.chev{top:2760px}

/* reviews */
.reviews{left:0;top:3007px;width:1200px;height:425px;
  background:
    radial-gradient(ellipse 260px 160px at 250px 120px,rgba(60,110,190,.55),rgba(60,110,190,0) 70%),
    radial-gradient(ellipse 260px 160px at 980px 110px,rgba(60,110,190,.55),rgba(60,110,190,0) 70%),
    var(--blue)}
.reviews-title{top:3068px;color:var(--white)}
.reviews-text{left:111px;top:3142px;width:978px;text-align:center;font-style:italic;font-size:14.5px;line-height:31px;color:var(--white)}
.reviews-name{left:0;width:1200px;top:3293px;text-align:center;color:var(--white);font-size:18px;font-weight:500}
.reviews-rule{left:575px;top:3322px;width:50px;height:2px;background:var(--white)}
.reviews-role{left:0;width:1200px;top:3340px;text-align:center;color:var(--white);font-size:14.5px}

/* footer */
.foot-col{top:3504px;font-size:13.5px;color:var(--muted);line-height:30px}
.foot-col h4{font-weight:500;font-size:14px;color:#222;margin-bottom:14px;letter-spacing:.3px}
.foot-contact li{list-style:none;display:flex;gap:14px;margin-bottom:10px}
.foot-contact svg{flex:none;margin-top:9px}
.foot-rule{left:111px;top:3725px;width:978px;height:2px;background:#777}
.copyright{left:113px;top:3760px;font-size:13.5px;color:#666}
.social{left:990px;top:3759px;display:flex;gap:12px}
.social span{width:18px;height:18px;border:1.5px solid #555;border-radius:4px}
</style>
</head>
<body>

<!-- header -->
<div class="abs topbar-email">
  <svg width="13" height="10" viewBox="0 0 13 10"><rect width="13" height="10" rx="1" fill="#c8913a"/><path d="M0 1l6.5 5L13 1" stroke="#fff" fill="none"/></svg>
  EMAIL- info@amberlanevantage.example
</div>
<div class="abs brand"><span class="brand-mark"></span><span class="brand-name">Amberlane Vantage Harbor</span></div>
<div class="abs topbar-call">
  <svg width="14" height="14" viewBox="0 0 14 14"><rect width="14" height="14" rx="2" fill="#c8913a"/><path d="M4 3l2 2-1 1.5c.6 1.2 1.3 1.9 2.5 2.5L9 8l2 2-1.5 1.5C6 11 3 8 2.5 4.5z" fill="#fff"/></svg>
  CALL US <b>555-014-2290</b>
</div>
<nav class="abs nav">
  <a class="active">HOME</a><a>ABOUT</a><a>SERVICES</a><a>WHY CHOOSE US</a><a>VIDEOS</a><a>BLOG AND NEWS</a><a>TESTIMONIALS</a><a>CONTACT US</a>
</nav>

<!-- hero -->
<div class="abs hero" role="img" aria-label="Colleagues working together around a laptop in a bright office"></div>
<div class="abs hero-panel"></div>
<h1 class="abs hero-title">Amberlane Vantage<br>Harbor</h1>
<p class="abs hero-text">Lorem ipsum dolor sit amet, consectetur adipiscing elit. Nulla sit amet tortor ac nibh faucibus elementum.</p>
<div class="abs hero-btn">GET STARTED</div>
<div class="abs hero-dots"><span class="on"></span><span></span><span></span><span></span></div>

<!-- what we do -->
<h2 class="abs section-title" style="top:747px">WHAT WE DO</h2>
<div class="abs round-arrow" style="left:55px;top:1061px"><svg width="12" height="18"><path d="M9 2L3 9l6 7" stroke="#222" stroke-width="2" fill="none"/></svg></div>
<div class="abs round-arrow" style="left:1100px;top:1073px"><svg width="12" height="18"><path d="M3 2l6 7-6 7" stroke="#222" stroke-width="2" fill="none"/></svg></div>

<div class="abs card" style="left:115px">
  <div class="card-photo" role="img" aria-label="Hand holding a tablet with digital marketing icons" style="background:radial-gradient(ellipse 80px 70px at 240px 140px,rgba(40,50,55,.8),rgba(40,50,55,0) 70%),radial-gradient(ellipse 90px 90px at 80px 190px,rgba(80,90,95,.6),rgba(80,90,95,0) 70%),linear-gradient(135deg,#eef1f1 0%,#c9d1d4 50%,#7d8b92 100%)"></div>
  <h3>LOREM IPSUM DOLOR SIT</h3>
  <p>Lorem ipsum dolor sit amet, adipiscing elit. Nulla sit amet tortor ac nibh faucibus elementum. Suspendisse potenti</p>
  <span class="btn-outline">READ MORE</span>
</div>
<div class="abs card" style="left:442px">
  <div class="card-photo" role="img" aria-label="Person working on a laptop showing charts" style="background:radial-gradient(ellipse 90px 70px at 200px 110px,rgba(225,225,225,.85),rgba(225,225,225,0) 70%),radial-gradient(ellipse 80px 80px at 60px 80px,rgba(40,50,60,.7),rgba(40,50,60,0) 70%),linear-gradient(135deg,#6b5848 0%,#7d6a58 50%,#3f332a 100%)"></div>
  <h3>LOREM IPSUM DOLOR SIT</h3>
  <p>Lorem ipsum dolor sit amet, adipiscing elit. Nulla sit amet tortor ac nibh faucibus elementum. Suspendisse potenti</p>
  <span class="btn-outline">READ MORE</span>
</div>
<div class="abs card" style="left:768px">
  <div class="card-photo" role="img" aria-label="Team reviewing documents on a wooden table" style="background:radial-gradient(ellipse 110px 60px at 150px 190px,rgba(240,238,234,.9),rgba(240,238,234,0) 70%),radial-gradient(ellipse 140px 80px at 150px 50px,rgba(150,95,55,.8),rgba(150,95,55,0) 70%),linear-gradient(180deg,#8a6a4e 0%,#a57f5c 45%,#4a3a30 100%)"></div>
  <h3>LOREM IPSUM DOLOR SIT</h3>
  <p>Lorem ipsum dolor sit amet, adipiscing elit. Nulla sit amet tortor ac nibh faucibus elementum. Suspendisse potenti</p>
  <span class="btn-outline">READ MORE</span>
</div>

<!-- video -->
<div class="abs video" role="img" aria-label="Aerial view of a stone wall winding across misty green mountain ridges"></div>
<h2 class="abs section-title video-title">OUR VIDEO</h2>
<div class="abs play"><svg width="36" height="40"><path d="M4 2l30 18L4 38z" fill="#fff"/></svg></div>
<div class="abs video-nav">
  <svg width="18" height="16"><path d="M8 2L2 8l6 6M2 8h15" stroke="#b0873c" stroke-width="2.5" fill="none"/></svg>
  <svg width="18" height="16"><path d="M10 2l6 6-6 6M16 8H1" stroke="#b0873c" stroke-width="2.5" fill="none"/></svg>
</div>

<!-- about -->
<h2 class="abs about-title">ABOUT US</h2>
<p class="abs about-text">Lorem ipsum dolor sit amet, consectetur adipiscing elit. Nulla sit amet tortor ac nibh faucibus elementum. Suspendisse potenti. Aenean bibendum lacus sodales mattis dictum. Nullam ultrices congue imperdiet. In lacinia, lorem id finibus iaculis, risus quam vehicula neque, a pellentesque tortor ante ut mi.Lorem ipsum dolor sit amet, consectetur adipiscing elit. Nulla sit amet</p>
<span class="abs btn-outline about-btn">READ MORE</span>
<div class="abs about-photo" role="img" aria-label="Two colleagues working at a laptop in an open office"></div>

<!-- blogs -->
<h2 class="abs section-title" style="top:2504px">LATEST BLOGS</h2>
<p class="abs blogs-sub">Nemo enim ipsam voluptatem quia voluptas sit aspernatur aut odit aut fugit,<br>sed quia consequuntur magni dolores</p>
<svg class="abs chev" style="left:86px" width="12" height="24"><path d="M10 2L2 12l8 10" stroke="#333" stroke-width="1.6" fill="none"/></svg>
<svg class="abs chev" style="left:1094px" width="12" height="24"><path d="M2 2l8 10-8 10" stroke="#333" stroke-width="1.6" fill="none"/></svg>

<div class="abs blog" style="left:111px;background:radial-gradient(ellipse 90px 90px at 120px 80px,rgba(50,60,80,.7),rgba(50,60,80,0) 70%),radial-gradient(ellipse 70px 60px at 270px 50px,rgba(190,40,40,.6),rgba(190,40,40,0) 70%),linear-gradient(180deg,#d8d5cf 0%,#9a8f82 55%,#3e3832 100%)" role="img" aria-label="Two colleagues discussing work at a desk">
  <div class="blog-body" style="bottom:14px">LOREM IPSUM DOLOR SIT AMET,<br>CONSECTETUR<br>14-10-2020</div>
</div>
<div class="abs blog" style="left:441px;background:radial-gradient(ellipse 90px 70px at 190px 60px,rgba(235,235,230,.75),rgba(235,235,230,0) 70%),linear-gradient(180deg,#7a5a48 0%,#5a463a 50%,#2f2924 100%)" role="img" aria-label="Presenter at a whiteboard during a marketing workshop">
  <div class="blog-body" style="top:92px">LOREM IPSUM DOLOR SIT AMET,<br>CONSECTETUR<br>14-10-2020
    <div class="more">READ MORE <svg width="14" height="14"><circle cx="7" cy="7" r="6" stroke="#fff" fill="none"/><path d="M6 4l3 3-3 3" stroke="#fff" fill="none"/></svg></div>
  </div>
</div>
<div class="abs blog" style="left:771px;background:radial-gradient(ellipse 110px 70px at 170px 70px,rgba(245,245,245,.9),rgba(245,245,245,0) 70%),radial-gradient(ellipse 140px 70px at 160px 200px,rgba(50,55,60,.7),rgba(50,55,60,0) 70%),linear-gradient(180deg,#c9cfcf 0%,#8f9593 60%,#4c524f 100%)" role="img" aria-label="Group seated in a training room facing a speaker">
  <div class="blog-body" style="bottom:14px">LOREM IPSUM DOLOR SIT AMET,<br>CONSECTETUR<br>14-10-2020</div>
</div>

<!-- reviews -->
<div class="abs reviews"></div>
<h2 class="abs section-title reviews-title">CLIENT REVIEWS</h2>
<p class="abs reviews-text">Lorem ipsum dolor sit amet, consectetur adipiscing elit. Nulla sit amet tortor ac nibh faucibus elementum. Suspendisse potenti. Aenean bibendum lacus sodales mattis dictum. Nullam ultrices congue imperdiet. In lacinia, lorem id finibus iaculis, risus quam vehicula neque, a pellentesque tortor ante ut mi.Lorem ipsum dolor sit amet, consectetur adipiscing elit. Nulla sit amet tortor ac nibh faucibus elementum. Suspendisse potenti. Aenean bibendum lacus sodales mattis dictum. Nullam ultrices congue imperdiet.</p>
<div class="abs reviews-name">Dana Whitlock</div>
<div class="abs reviews-rule"></div>
<div class="abs reviews-role">Lorem ipsum dolor</div>

<!-- footer -->
<div class="abs foot-col" style="left:111px;width:270px">
  <h4>ABOUT US</h4>
  <p style="font-size:12.5px">Nemo enim ipsam voluptatem quia voluptas<br>sit aspernatur aut odit aut fugit, sed quia<br>consequuntur magni dolores eos qui</p>
</div>
<div class="abs foot-col" style="left:428px">
  <h4>SERVICES</h4>
  <p>Lorem ipsum dolor<br>Lorem ipsum dolor<br>Lorem ipsum dolor<br>Lorem ipsum dolor</p>
</div>
<div class="abs foot-col" style="left:677px">
  <h4>QUICK LINKS</h4>
  <p>Home<br>About<br>Services<br>Blogs<br>Contact</p>
</div>
<div class="abs foot-col" style="left:881px;width:210px">
  <h4>CONTACT US</h4>
  <ul class="foot-contact">
    <li><svg width="14" height="14" viewBox="0 0 14 14"><path d="M3 1l2.5 2.5-1.2 1.8c.8 1.6 1.8 2.6 3.4 3.4l1.8-1.2L12 10l-1.8 2C5.5 11.5 2.5 8.5 1 3.8z" stroke="#333" fill="none"/></svg>555-018-3344</li>
    <li><svg width="14" height="16" viewBox="0 0 14 16"><path d="M7 15S2 9.5 2 6a5 5 0 0110 0c0 3.5-5 9-5 9z" fill="#222"/><circle cx="7" cy="6" r="2" fill="#fff"/></svg>14500 Lorem ipsum dolor<br>sit amet,eiusmod</li>
    <li><svg width="14" height="11" viewBox="0 0 14 11"><rect x=".5" y=".5" width="13" height="10" stroke="#333" fill="none"/><path d="M.5 .5L7 6l6.5-5.5" stroke="#333" fill="none"/></svg>info@amberlanevantage<br>.example</li>
  </ul>
</div>
<div class="abs foot-rule"></div>
<div class="abs copyright">© 2020 All Rights Reserved</div>
<div class="abs social"><span></span><span></span><span></span><span></span></div>

</body>
</html>
```